Real Estate Investor needs awesome business card design

I invest in real estate, focused on multi-family properties, and I need a business card to hand out to potential partners. I prefer simple, clean designs, but it needs to stand out, so I'd like there to be a bit of red in the design as well.

It should include this information:

Front
Dallin Pecksworth
Real Estate Investor
Direct phone: 502-867-3394
Email: dallinhpecksworth@quillmail.example
Headshot (Picture), I've uploaded a few, just pick the one you think looks best with your design. You can remove the background from the headshot image if it looks better.

Back
The back of the card's design should flow and be congruent with the front. On the back I want to put an inspirational quote or question. There will be different ones depending on the card, so I'll need the original file so I can edit it in the end.

For now, use “The Pessimist Sees Difficulty In Every Opportunity. The Optimist Sees The Opportunity In Every Difficulty.” -Barnaby Ellsworth

Target Market(s)

Investors

Industry/Entity Type

Real Estate

Contact Information for Business Card

Front
Dallin Pecksworth
Real Estate Investor

Back
The back of the card's design should flow and be congruent with the front. On the back I want to put an inspirational quote or question. There will be different ones depending on the card, so I'll need the original file so I can edit it in the end. I've uploaded some EXAMPLES of business cards with quotes on them. Don't copy but feel free to use them as inspiration.

The design will be printed on "ZIB sized" business cards
1039 x 697 pixels
with rounded corners

Font styles to use
Serif
Decorative
Script

Colors
ec1f27

Requirements
Must have
• Headshot, name, and other information in it.
• 1039 x 697 pixels
• Rounded corners
• Clean design that pops. I'm open to see any color background, including black.
• Headshots can be located here: https://www.filecrate.example/sh/8kd2wq7mzt31hvx/BBQTXP4ruf9LmQ0KhcvWx7b?dl=0
Nice to have
• It would be awesome if the design included a personal signature or monogram, but if not I'll get a personal logo developed later and the card redesigned if I think it needs it.
Should not have
• Cluttered design

```html
<!DOCTYPE html>
<html lang="en">
<head>
<meta charset="utf-8">
<title>Dallin Pecksworth – Business Card</title>
<link rel="stylesheet" href="https://fonts.googleapis.com/css2?family=Gelasio:ital,wght@0,400;0,500;1,700&display=swap">
<style>
  :root {
    --page-bg: #ececec;
    --card-white: #ffffff;
    --card-dark: #1c1c1c;
    --ink: #1a1a1a;
    --ink-light: #f4f4f4;
    --accent: #ec1f27;
    --photo-light: #5a5a5a;
    --photo-dark: #111111;
  }
  * { box-sizing: border-box; margin: 0; padding: 0; }
  html, body {
    width: 1200px;
    height: 942px;
    overflow: hidden;
    background: var(--page-bg);
    font-family: "Gelasio", Georgia, serif;
  }
  .canvas {
    position: relative;
    width: 1200px;
    height: 942px;
  }
  .card {
    position: absolute;
    left: 277px;
    width: 646px;
    height: 391px;
    border-radius: 14px;
    overflow: hidden;
    box-shadow: 0 4px 14px rgba(0, 0, 0, 0.18);
  }
  .card--back {
    top: 65px;
    background: var(--card-white);
    display: flex;
    align-items: center;
    justify-content: center;
  }
  .quote {
    text-align: center;
    color: var(--ink);
    font-size: 16.5px;
    line-height: 24px;
    margin-top: -37px;
  }
  .quote__author {
    display: block;
    color: var(--accent);
    font-style: italic;
    font-weight: 700;
    font-size: 17px;
    letter-spacing: 0.3px;
    margin-top: 1px;
  }
  .card--front {
    top: 485px;
    background: var(--card-dark);
  }
  .headshot {
    position: absolute;
    left: 7px;
    top: 6px;
    width: 296px;
    height: 385px;
    background: radial-gradient(ellipse 60% 55% at 50% 70%, var(--photo-light) 0%, #2a2a2a 60%, var(--photo-dark) 100%);
    clip-path: polygon(35% 0, 65% 0, 72% 28%, 95% 45%, 100% 100%, 0 100%, 5% 45%, 28% 28%);
  }
  .contact {
    position: absolute;
    left: 322px;
    top: 141px;
    color: var(--ink-light);
    white-space: nowrap;
  }
  .contact__name {
    color: var(--accent);
    font-size: 26px;
    font-weight: 400;
    line-height: 30px;
  }
  .contact__role {
    font-size: 16px;
    line-height: 20px;
    margin-bottom: 11px;
  }
  .contact__line {
    font-size: 15px;
    line-height: 21px;
  }
  .contact__label { color: var(--accent); }
</style>
</head>
<body>
  <main class="canvas">
    <section class="card card--back" aria-label="Card back">
      <p class="quote">
        The Pessimist Sees Difficulty In Every Opportunity.<br>
        The Optimist Sees The Opportunity In Every Difficulty.
        <span class="quote__author">BARNABY ELLSWORTH</span>
      </p>
    </section>

    <section class="card card--front" aria-label="Card front">
      <div class="headshot" role="img" aria-label="Black and white headshot of Dallin Pecksworth in a dark blazer"></div>
      <div class="contact">
        <h1 class="contact__name">Dallin Pecksworth</h1>
        <p class="contact__role">Real Estate Investor</p>
        <p class="contact__line"><span class="contact__label">P:</span> 502-867-3394</p>
        <p class="contact__line"><span class="contact__label">E:</span> dallinhpecksworth@quillmail.example</p>
      </div>
    </section>
  </main>
</body>
</html>
```